Facebook & Instagram Ad Design for Chiropractor

I'd like a series of ads developed for our chiropractic office to use on Facebook and Instagram. I've attached the versions we're using today. They need to be updated. The offer content would be generally the same. There are two types of ads we're seeking. One for basic chiropractic services and the other for chiropractic decompression services.

Current ads can be seen in attached and here:
https://lnk.example/8TrQ2zXvPoLkm3A

Learn more about the company at www.bellwingchiropractic.example

Target Market(s)

Potential patients seeking chiropractic care or who are unaware that chiropractic could help them (suffer from back pain, etc.) in the greater Green Bay, WI area.

Industry/Entity Type

Chiropractic

Font styles to use
Sans Serif

Colors
0592cd
3277b5

Requirements
Must have
• Compelling visuals
Comply with text requirements for FB & Insta ads
Should not have
• Clinical images that depict traditional medical care

```html
<!DOCTYPE html>
<html lang="en">
<head>
<meta charset="utf-8">
<title>Bellwing Chiropractic – New Patient Ads</title>
<link rel="stylesheet" href="https://fonts.googleapis.com/css2?family=Yanone+Kaffeesatz:wght@600;700&family=Questrial&display=swap">
<style>
  :root{
    --cyan:#0592cd;
    --blue:#3277b5;
    --royal:#1f5fa8;
    --ocean:#0a7fc0;
    --navy:#0b3a5c;
    --ink:#1c2b45;
    --sky:#7fd0f5;
    --pale:#cfe6fd;
    --link:#1a5ea8;
    --white:#ffffff;
    --rule:#7a1f2b;
  }
  *{box-sizing:border-box;margin:0;padding:0}
  html,body{width:1200px;height:734px;overflow:hidden;background:var(--white)}
  .canvas{position:relative;width:1200px;height:734px;background:var(--white)}
  .ad{position:absolute;overflow:hidden;box-shadow:0 1px 5px rgba(0,0,0,.18)}
  .ad svg.shapes{position:absolute;inset:0;width:100%;height:100%}
  .ad > *{position:absolute}
  .brand{font-family:"Yanone Kaffeesatz",sans-serif;font-weight:700;font-size:31px;line-height:1;white-space:nowrap;border-bottom:1.5px solid currentColor;padding-bottom:2px}
  .headline{font-family:"Yanone Kaffeesatz",sans-serif;font-weight:600;font-size:29px;line-height:34px;text-transform:uppercase}
  .price{font-family:"Yanone Kaffeesatz",sans-serif;font-weight:600;font-size:24px;color:var(--white);line-height:1}
  .cta{font-family:"Questrial",sans-serif;font-weight:700;color:var(--link);white-space:nowrap}

  /* Ad one */
  .ad-one{left:49px;top:53px;width:561px;height:294px;background:var(--white)}
  .ad-one .brand{left:16px;top:43px;color:var(--ink);border-color:var(--rule)}
  .ad-one .headline{left:18px;top:96px;color:var(--cyan)}
  .ad-one .price{left:32px;top:187px}
  .ad-one .cta{left:19px;top:234px;font-size:15px}

  /* Ad two */
  .ad-two{left:650px;top:53px;width:505px;height:265px;background:var(--white)}
  .ad-two .brand{left:20px;top:29px;color:var(--white)}
  .ad-two .headline{left:19px;top:93px;color:var(--white)}
  .ad-two .price{left:19px;top:187px}
  .ad-two .cta{left:0;width:100%;text-align:center;top:233px;font-size:15px;text-transform:uppercase}

  /* Ad three */
  .ad-three{left:49px;top:390px;width:561px;height:294px;background:var(--blue)}
  .ad-three .brand{left:333px;top:35px;color:var(--white)}
  .ad-three .service{left:333px;top:82px;font-family:"Questrial",sans-serif;color:var(--white);font-weight:700;font-size:21px;line-height:1.2;white-space:nowrap}
  .ad-three .service small{display:block;font-size:17px;margin-top:3px}
  .ad-three .special{left:341px;top:164px;font-family:"Questrial",sans-serif;font-weight:700;font-size:15px;color:var(--blue);white-space:nowrap}
  .ad-three .button{left:333px;top:214px;width:82px;height:34px;border:1.5px solid var(--white);color:var(--white);font-family:"Questrial",sans-serif;font-size:12.5px;display:flex;align-items:center;justify-content:center}

  /* Ad four */
  .ad-four{left:650px;top:351px;width:505px;height:265px;background:var(--white)}
  .ad-four .brand{left:20px;top:30px;color:var(--white)}
  .ad-four .headline{left:23px;top:83px;color:var(--white)}
  .ad-four .price{left:92px;top:178px}
  .ad-four .cta{left:300px;width:176px;text-align:center;top:230px;font-size:15px;text-transform:uppercase}
</style>
</head>
<body>
<main class="canvas">

  <section class="ad ad-one" aria-label="New patient special ad, white layout">
    <svg class="shapes" viewBox="0 0 561 294" aria-hidden="false">
      <defs>
        <linearGradient id="photoOne" x1="0" y1="0" x2="1" y2="1">
          <stop offset="0" stop-color="#c9cdd6"/><stop offset=".45" stop-color="#e8e6e4"/><stop offset="1" stop-color="#2f7fd6"/>
        </linearGradient>
      </defs>
      <path d="M203 0 L380 0 L275 92 Z" fill="var(--blue)"/>
      <path role="img" aria-label="Photo: chiropractor adjusting the neck of a woman lying on a blue mat" d="M330 0 Q252 60 254 150 Q258 250 323 294 L561 294 L561 0 Z" fill="url(#photoOne)" stroke="var(--blue)" stroke-width="2"/>
      <path d="M19 175 L115 175 L97 215 L19 215 Z" fill="var(--blue)"/>
    </svg>
    <h2 class="brand">Bellwing Chiropractic</h2>
    <p class="headline">New Patient Special<br>Offer</p>
    <p class="price">$25%</p>
    <p class="cta">Get This Offer Today!</p>
  </section>

  <section class="ad ad-two" aria-label="New patient special ad, blue layout with circle">
    <svg class="shapes" viewBox="0 0 505 265">
      <defs>
        <linearGradient id="photoTwo" x1="0" y1="0" x2="1" y2="1">
          <stop offset="0" stop-color="#e7d7cd"/><stop offset=".5" stop-color="#c9a893"/><stop offset="1" stop-color="#3b3f48"/>
        </linearGradient>
      </defs>
      <rect width="505" height="220" fill="var(--ocean)"/>
      <path d="M0 17 L269 17 L245 76 L0 76 Z" fill="var(--navy)"/>
      <path d="M272 17 L276 17 L252 76 L248 76 Z" fill="var(--sky)"/>
      <circle cx="401" cy="94" r="128" fill="var(--sky)"/>
      <circle cx="403" cy="92" r="120" fill="var(--ocean)"/>
      <circle cx="406" cy="96" r="110" fill="var(--blue)"/>
      <circle role="img" aria-label="Photo: hands massaging the upper back of a woman in a sports top" cx="413" cy="94" r="104" fill="url(#photoTwo)"/>
      <path d="M0 177 L100 177 L82 220 L0 220 Z" fill="var(--navy)"/>
      <path d="M103 177 L106 177 L88 220 L85 220 Z" fill="var(--sky)"/>
    </svg>
    <h2 class="brand">Bellwing Chiropractic</h2>
    <p class="headline">New Patient Special<br>Offer</p>
    <p class="price">$25%</p>
    <p class="cta">Get this offer today!</p>
  </section>

  <section class="ad ad-three" aria-label="Spinal decompression ad">
    <svg class="shapes" viewBox="0 0 561 294">
      <defs>
        <linearGradient id="photoThree" x1="0" y1="0" x2="1" y2="0">
          <stop offset="0" stop-color="#3a4a66"/><stop offset=".45" stop-color="#52627d"/><stop offset="1" stop-color="#e4e6ea"/>
        </linearGradient>
      </defs>
      <path d="M0 0 L312 0 Q330 60 300 130 Q258 210 300 294 L0 294 Z" fill="var(--sky)"/>
      <path role="img" aria-label="Photo: practitioner in a white coat examining a patient's shoulder and arm" d="M0 0 L303 0 Q318 60 288 130 Q248 210 293 294 L0 294 Z" fill="url(#photoThree)"/>
      <path d="M333 151 L536 151 L518 198 L333 198 Z" fill="var(--pale)"/>
    </svg>
    <h2 class="brand">Bellwing Chiropractic</h2>
    <p class="service">Spinal Decompression<small>Therapy in Green Bay</small></p>
    <p class="special">New Patient Special $25</p>
    <p class="button">GET OFFER</p>
  </section>

  <section class="ad ad-four" aria-label="New patient special ad, hexagon layout">
    <svg class="shapes" viewBox="0 0 505 265">
      <defs>
        <linearGradient id="photoFour" x1="0" y1="0" x2="0" y2="1">
          <stop offset="0" stop-color="#f1f3f4"/><stop offset=".6" stop-color="#d9dcdf"/><stop offset="1" stop-color="#3b9fd9"/>
        </linearGradient>
      </defs>
      <path d="M0 0 L505 0 L505 158 L400 70 Q300 150 230 205 Q120 260 0 175 Z" fill="#cfe0f2"/>
      <path d="M0 0 L505 0 L505 152 L400 64 Q300 140 225 190 Q120 245 0 166 Z" fill="#6d9fd6"/>
      <path d="M0 0 L505 0 L505 146 L400 60 Q300 130 220 178 Q115 230 0 158 Z" fill="var(--royal)"/>
      <path d="M57 210 Q60 162 122 162 Q184 162 187 210 Z" fill="var(--navy)"/>
      <polygon points="388,20 472,68 472,164 388,212 304,164 304,68" fill="var(--cyan)"/>
      <polygon role="img" aria-label="Photo: chiropractor treating a woman lying on a blue mat in a bright studio" points="388,28 465,72 465,160 388,204 311,160 311,72" fill="url(#photoFour)" stroke="var(--white)" stroke-width="2"/>
    </svg>
    <h2 class="brand">Bellwing Chiropractic</h2>
    <p class="headline">New Patient Special<br>Offer</p>
    <p class="price">$25%</p>
    <p class="cta">Get this offer today!</p>
  </section>

</main>
</body>
</html>
```